Business card for real estate agent / office

We're looking for a new business card. We want something that is pretty clean, modern and sleek. Something that also tells people that we are a new age company...cutting edge. Although real estate has been done a certain way the last 100 years, we have energy and vibrance. Company name is Bright Harbor Properties. info can be found here: http://www.bhprealestate.example/

needs to include: Name, title, phone number, email. our license number also needs to be displayed somewhere.

Target Market(s)

25-55 homeowners or potential homeowners

Industry/Entity Type

Business

Contact Information for Business Card

we need business card designs for real estate agent / office

Font styles to use
Serif

Requirements
Must have
• needs to include: Name, title, phone number, email. our license number also needs to be displayed somewhere and company name.
Nice to have
• placement area for photo

```html
<!DOCTYPE html>
<html lang="en">
<head>
<meta charset="utf-8">
<title>Bright Harbor Properties – Business Card</title>
<link rel="stylesheet" href="https://fonts.googleapis.com/css2?family=Noto+Serif:wght@400;700&display=swap">
<style>
  :root {
    --navy: #07476b;
    --navy-dark: #0b3a5c;
    --green: #5cbb46;
    --white: #ffffff;
    --stage: #e9ebee;
    --ink-soft: #3b4a57;
  }
  * { box-sizing: border-box; margin: 0; padding: 0; }
  html, body {
    width: 1200px; height: 880px; overflow: hidden;
    background: var(--stage);
    font-family: "Noto Serif", Georgia, serif;
  }
  .canvas {
    position: relative; width: 1200px; height: 880px;
    display: flex; flex-direction: column; align-items: center; justify-content: center; gap: 40px;
  }
  .card {
    position: relative; width: 700px; height: 400px;
    box-shadow: 0 6px 20px rgba(0,0,0,.15);
  }

  /* Back side */
  .card-back {
    background: var(--navy);
    display: flex; flex-direction: column; align-items: center; justify-content: center;
    color: var(--white); text-align: center;
  }
  .brand-mark { display: flex; align-items: center; gap: 14px; }
  .brand-mark .dot { width: 22px; height: 22px; background: currentColor; }
  .brand-name { font-weight: 700; font-size: 40px; line-height: 1.1; }
  .card-back .tagline { margin-top: 34px; font-size: 20px; letter-spacing: .3px; }

  /* Front side */
  .card-front { background: var(--white); }
  .card-front .brand-mark {
    position: absolute; top: 46px; right: 44px; color: var(--navy);
  }
  .card-front .brand-name { font-size: 26px; }
  .card-front .brand-mark .dot { width: 16px; height: 16px; background: var(--green); }
  .agent { position: absolute; left: 44px; top: 128px; }
  .agent-name { color: var(--navy-dark); font-weight: 700; font-size: 24px; letter-spacing: .5px; }
  .agent-title { color: var(--green); font-size: 18px; margin-top: 2px; }
  .agent-license { color: var(--ink-soft); font-size: 14px; margin-top: 4px; letter-spacing: .3px; }
  .website {
    position: absolute; right: 44px; top: 242px; font-size: 17px; color: var(--navy);
  }
  .website .domain { color: var(--green); }
  .rule {
    position: absolute; left: 200px; right: 44px; top: 278px; height: 2px; background: var(--green);
  }
  .contact { position: absolute; left: 44px; bottom: 34px; list-style: none; }
  .contact li {
    display: flex; align-items: center; gap: 10px;
    font-size: 18px; color: var(--navy-dark); line-height: 1.5;
  }
  .contact .icon { width: 20px; height: 20px; flex: none; }
</style>
</head>
<body>
<main class="canvas">
  <section class="card card-back">
    <div class="brand-mark">
      <span class="dot"></span>
      <span class="brand-name">Bright Harbor Properties</span>
    </div>
    <p class="tagline">We Greatly Appreciate Your Referrals</p>
  </section>

  <section class="card card-front">
    <div class="agent">
      <h1 class="agent-name">DANIEL WHITAKER</h1>
      <p class="agent-title">Real Estate Broker, Realtor, MBA</p>
      <p class="agent-license">License # 01928374</p>
    </div>
    <div class="brand-mark">
      <span class="dot"></span>
      <span class="brand-name">Bright Harbor Properties</span>
    </div>
    <p class="website">www.<span class="domain">brightharborprop</span>.example</p>
    <div class="rule"></div>
    <ul class="contact">
      <li>
        <svg class="icon" viewBox="0 0 20 20" aria-hidden="true">
          <rect width="20" height="20" fill="#5cbb46"/>
          <path d="M6 4c1 0 1.5 2.5 1.5 3S6.5 8 6.5 8.5c.5 1.5 3.5 4.5 5 5 .5 0 1-1 1.5-1s3 .5 3 1.5-1 2-2 2C9 16 4 11 4 6c0-1 1-2 2-2z" fill="#fff"/>
        </svg>
        555-014-2286
      </li>
      <li>
        <svg class="icon" viewBox="0 0 20 20" aria-hidden="true">
          <rect width="20" height="20" fill="#5cbb46"/>
          <rect x="4" y="6" width="12" height="8" fill="none" stroke="#fff" stroke-width="1.4"/>
          <path d="M4 6l6 5 6-5" fill="none" stroke="#fff" stroke-width="1.4"/>
        </svg>
        info@bhprealestate.example
      </li>
    </ul>
  </section>
</main>
</body>
</html>
```